Business Card Design

We have recently seen two business cards that caught our attention and think the designs would work for us. We are an accounting firm that serves small businesses in a variety of industries. Attached are the two business card that inspired us along with very rough layouts. We would like to see a professional layout using our company information.

Industry/Entity Type

Accounting

Contact Information for Business Card

Company Name - Dalworth Pryce
Address - 4180 Brambleton Lane, Suite 310, Houston, TX 77051
713-508-9627 - Main
281-369-0714 - Fax

Team Member Names, emails and phone numbers (see attachment)

```html
<!DOCTYPE html>
<html lang="en">
<head>
<meta charset="utf-8">
<title>Dalworth Pryce – Business Card</title>
<link rel="stylesheet" href="https://fonts.googleapis.com/css2?family=Lato:wght@400;700;900&display=swap">
<style>
  :root {
    --backdrop: #2b2b2b;
    --band: #070707;
    --panel-light: #f6f6f6;
    --panel-mid: #d9d9d9;
    --ink: #111111;
    --muted: #9a9a9a;
    --band-text: #e6e6e6;
    --white: #ffffff;
  }
  * { box-sizing: border-box; margin: 0; padding: 0; }
  html, body {
    width: 1200px; height: 900px; overflow: hidden;
    background: var(--backdrop);
    font-family: "Lato", sans-serif;
  }
  .card {
    position: absolute;
    left: 100px; top: 165px;
    width: 1000px; height: 570px;
    border-radius: 30px;
    overflow: hidden;
    background: linear-gradient(160deg, var(--panel-light) 0%, var(--white) 45%, var(--panel-mid) 100%);
    box-shadow: 0 20px 50px rgba(0,0,0,.55);
  }
  .card-header {
    height: 96px;
    background: var(--band);
    display: flex; align-items: center; justify-content: center;
  }
  .company-name {
    color: var(--white);
    font-weight: 900;
    font-size: 40px;
    letter-spacing: 1px;
    text-transform: uppercase;
  }
  .card-body {
    position: relative;
    height: 324px;
  }
  .brand-mark {
    position: absolute;
    left: 90px; top: 128px;
    display: flex; align-items: center; gap: 18px;
  }
  .brand-mark .square {
    width: 48px; height: 48px; background: var(--ink);
  }
  .brand-mark .brand-name {
    color: var(--ink);
    font-weight: 900;
    font-size: 44px;
    letter-spacing: .5px;
    white-space: nowrap;
  }
  .person {
    position: absolute;
    left: 560px; top: 58px;
  }
  .person-name {
    font-weight: 900; font-size: 34px; color: var(--ink);
    text-transform: uppercase; line-height: 1;
    white-space: nowrap;
  }
  .person-title {
    font-weight: 400; font-size: 22px; color: var(--muted);
    text-transform: uppercase; letter-spacing: 1px; margin-top: 4px;
  }
  .person-line {
    display: flex; align-items: center; gap: 10px;
    font-weight: 700; font-size: 24px; color: var(--ink);
    margin-top: 10px;
    white-space: nowrap;
  }
  .person-line svg { width: 22px; height: 22px; fill: var(--ink); flex: none; }
  .card-footer {
    height: 150px;
    background: var(--band);
    position: relative;
    color: var(--band-text);
    font-weight: 400;
    font-size: 28px;
  }
  .footer-item {
    position: absolute;
    display: flex; align-items: center; gap: 14px;
    white-space: nowrap;
    line-height: 1.2;
  }
  .footer-item svg { width: 28px; height: 28px; fill: var(--band-text); flex: none; }
  .main-phone { left: 270px; top: 32px; }
  .fax { left: 620px; top: 32px; }
  .address { left: 270px; top: 86px; }
</style>
</head>
<body>
  <section class="card">
    <header class="card-header">
      <h1 class="company-name">Dalworth Pryce</h1>
    </header>

    <div class="card-body">
      <div class="brand-mark">
        <span class="square"></span>
        <span class="brand-name">Dalworth Pryce</span>
      </div>

      <div class="person">
        <p class="person-name">Marisol Hart</p>
        <p class="person-title">Account Manager</p>
        <p class="person-line">
          <svg viewBox="0 0 24 24" aria-hidden="true"><path d="M7 1h10a2 2 0 0 1 2 2v18a2 2 0 0 1-2 2H7a2 2 0 0 1-2-2V3a2 2 0 0 1 2-2zm0 3v15h10V4H7zm5 16.2a1 1 0 1 0 0 .1z"/></svg>
          832-417-2958
        </p>
        <p class="person-line">
          <svg viewBox="0 0 24 24" aria-hidden="true"><path d="M2 5h20v14H2V5zm2 2v.4l8 5.6 8-5.6V7H4zm0 2.8V17h16V9.8l-8 5.6-8-5.6z"/></svg>
          mhart@dalworthpryce.com
        </p>
      </div>
    </div>

    <footer class="card-footer">
      <p class="footer-item main-phone">
        <svg viewBox="0 0 24 24" aria-hidden="true"><path d="M3 8c0-2 4-4 9-4s9 2 9 4v2h-4V8c-1-.6-3-1-5-1s-4 .4-5 1v2H3V8zm4 3h10l3 9H4l3-9zm5 2a3 3 0 1 0 0 6 3 3 0 0 0 0-6z"/></svg>
        713-508-9627
      </p>
      <p class="footer-item fax">
        <svg viewBox="0 0 24 24" aria-hidden="true"><path d="M6 2h12v6H6V2zm-3 7h18v9h-3v4H6v-4H3V9zm5 7v4h8v-4H8zm10-5a1 1 0 1 0 0 2 1 1 0 0 0 0-2z"/></svg>
        281-369-0714
      </p>
      <p class="footer-item address">
        <svg viewBox="0 0 24 24" aria-hidden="true"><path d="M12 3l10 9h-3v9h-5v-6h-4v6H5v-9H2l10-9z"/></svg>
        4180 Brambleton Lane, Suite 310, Houston, TX 77051
      </p>
    </footer>
  </section>
</body>
</html>
```